Business Cards for IT Consulting Company (Managed Service Provider)

I am looking to have some business cards printed and would like some designs. We are an IT Consulting company based in Vancouver BC. I would like a nice clean and modern look to the cards. I have uploaded all the versions of my logo so parts can be used as needed. Here is a snippit from our website homepage:

Kelbrook Systems Ltd. is an IT Solutions Partner located in Vancouver BC, Canada. We offer IT solutions and support to customers in the greater Vancouver Area. With expertise in Microsoft platforms, as well as Linux and Mac OSX and over 12 years experience in the IT industry, Kelbrook Systems is dedicated to offering our clients top quality service and products. We take pride in the solutions we offer our customers. The greatest compliment a client can give us is to recommend our services.

Kelbrook Systems Ltd. offers a wide range of IT services from onsite service to remote support and managed service solutions. This allows clients to choose the support path that best suits their company’s needs. Supporting many different sized companies from small to enterprise level over the past 12 years Kelbrook Systems has the experience and expertise needed to ensure things run smoothly. Allowing our clients to focus on doing business.

Revolutionizing the way IT services are delivered.

Kelbrook Systems is dedicated to providing our clients with IT solutions that work and grow with them for years to come. This philosophy helps save money in the long run instead of replacing equipment constantly. Far too often IT solutions are not well thought out and while possibly solving the problem at hand, require replacement due to growth or quality within a very short time frame. Kelbrook Systems takes pride in providing solutions that will last and be able to accommodate growth without the need for replacement.

Industry/Entity Type

Information Technology

Contact Information for Business Card

Kelbrook Systems Ltd.
(Employee Name)
Eml: (Employees Email Address)
Web: kelbrook.me
Ph: 604-555-0142

Font styles to use
Serif
Sans Serif

Requirements
Must have
• The Company logo and company colors.
Nice to have
• - Our tag line: "Dependable IT Solutions" or "Revolutionizing the way IT services are delivered."
• - Also I really like the idea of nature and technology together blending which is sort of where my logo came from so integrating that somehow onto the business cards would be great.

```html
<!DOCTYPE html>
<html lang="en">
<head>
<meta charset="utf-8">
<title>Kelbrook Systems Ltd. — Business Card</title>
<link rel="stylesheet" href="https://fonts.googleapis.com/css2?family=Raleway:wght@400;500;600&display=swap">
<style>
  :root {
    --bg: #c9e8de;
    --card-black: #050505;
    --brand-blue: #00a9df;
    --text-white: #ffffff;
    --text-grey: #6f6f6f;
    --card-radius: 30px;
  }
  * { box-sizing: border-box; margin: 0; padding: 0; }
  html, body { width: 1200px; height: 856px; overflow: hidden; }
  body {
    background: var(--bg);
    font-family: "Raleway", "Helvetica Neue", Arial, sans-serif;
    display: flex;
    flex-direction: column;
    align-items: center;
    justify-content: center;
    gap: 48px;
  }
  .card {
    width: 620px;
    height: 354px;
    border-radius: var(--card-radius);
    overflow: hidden;
    box-shadow: 0 10px 24px rgba(0, 60, 50, 0.18);
  }

  /* Back side */
  .card-back {
    background: var(--card-black);
    display: flex;
    flex-direction: column;
    align-items: center;
    justify-content: center;
    gap: 46px;
  }
  .brand {
    display: flex;
    align-items: center;
    gap: 18px;
    color: var(--brand-blue);
    font-weight: 600;
    white-space: nowrap;
  }
  .brand-mark {
    border: 4px solid var(--brand-blue);
    flex: none;
  }
  .card-back .brand-mark { width: 46px; height: 46px; }
  .card-back .brand-name { font-size: 38px; letter-spacing: 0.5px; }
  .back-web {
    color: var(--text-grey);
    font-size: 26px;
    letter-spacing: 1px;
  }

  /* Front side */
  .card-front { display: flex; }
  .front-brand-panel {
    width: 38%;
    background: var(--card-black);
    display: flex;
    align-items: center;
    justify-content: center;
    padding: 0 14px;
  }
  .card-front .brand { gap: 9px; }
  .card-front .brand-mark { width: 20px; height: 20px; border-width: 3px; }
  .card-front .brand-name { font-size: 16px; }
  .front-info-panel {
    flex: 1;
    background: var(--brand-blue);
    color: var(--text-white);
    padding: 52px 36px 36px 44px;
    display: flex;
    flex-direction: column;
  }
  .person-name {
    font-size: 32px;
    font-weight: 400;
    letter-spacing: 1px;
    margin-bottom: 26px;
  }
  .contact-list { list-style: none; display: flex; flex-direction: column; gap: 12px; }
  .contact-item {
    display: flex;
    align-items: center;
    gap: 14px;
    font-size: 18px;
    white-space: nowrap;
  }
  .contact-icon {
    width: 28px;
    height: 28px;
    border-radius: 50%;
    background: var(--text-white);
    display: flex;
    align-items: center;
    justify-content: center;
    flex: none;
  }
  .contact-icon svg { width: 16px; height: 16px; }
  .tagline {
    margin-top: auto;
    font-size: 22px;
    letter-spacing: 0.5px;
  }
</style>
</head>
<body>

  <section class="card card-back" aria-label="Card back">
    <div class="brand">
      <span class="brand-mark"></span>
      <span class="brand-name">Kelbrook Systems Ltd.</span>
    </div>
    <p class="back-web">www.kelbrook.me</p>
  </section>

  <section class="card card-front" aria-label="Card front">
    <div class="front-brand-panel">
      <div class="brand">
        <span class="brand-mark"></span>
        <span class="brand-name">Kelbrook Systems Ltd.</span>
      </div>
    </div>
    <div class="front-info-panel">
      <h1 class="person-name">DANA WHITLOW</h1>
      <ul class="contact-list">
        <li class="contact-item">
          <span class="contact-icon">
            <svg viewBox="0 0 16 16"><rect x="2" y="4" width="12" height="8" rx="1" fill="none" stroke="#00a9df" stroke-width="1.5"/><path d="M2.5 4.5 8 9l5.5-4.5" fill="none" stroke="#00a9df" stroke-width="1.5"/></svg>
          </span>
          dana.whitlow@kelbrook.me
        </li>
        <li class="contact-item">
          <span class="contact-icon">
            <svg viewBox="0 0 16 16"><circle cx="8" cy="8" r="6" fill="none" stroke="#00a9df" stroke-width="1.4"/><ellipse cx="8" cy="8" rx="2.6" ry="6" fill="none" stroke="#00a9df" stroke-width="1.2"/><path d="M2 8h12" stroke="#00a9df" stroke-width="1.2"/></svg>
          </span>
          kelbrook.me
        </li>
        <li class="contact-item">
          <span class="contact-icon">
            <svg viewBox="0 0 16 16"><path d="M4.2 2.2 6.3 4.6 5.2 6.2c.8 1.8 2.2 3.2 4 4l1.6-1.1 2.4 2.1-1.3 2c-4.8-.4-8.7-4.3-9.1-9.1z" fill="#00a9df"/></svg>
          </span>
          604-555-0142
        </li>
      </ul>
      <p class="tagline">Dependable IT Solutions</p>
    </div>
  </section>

</body>
</html>
```